Brambury Logistics

Create a modern, simple, Elegant business card design for my business.

Services: Tamo Trucks, Transport, Contract Logistics,

Industry/Entity Type

Business

Contact Information for Business Card

Include all details same as old card plus new website address: www.bramburylogistics.com.au

Requirements
Must have
• Similar colors to Logo.

```html
<!DOCTYPE html>
<html lang="en">
<head>
<meta charset="utf-8">
<title>Brambury Logistics – Business Card</title>
<link rel="stylesheet" href="https://fonts.googleapis.com/css2?family=Roboto+Condensed:wght@400;700&display=swap">
<style>
  :root {
    --page-bg: #e9ebee;
    --card-white: #f7f8f9;
    --swoosh-grey: #b9bcc0;
    --logo-grey: #7d8186;
    --blue-light: #22b6d6;
    --blue-mid: #1a8fc0;
    --blue-deep: #146ea7;
    --ink-white: #ffffff;
    --card-radius: 18px;
    --font-text: "Roboto Condensed", "Arial Narrow", sans-serif;
  }
  * { box-sizing: border-box; margin: 0; padding: 0; }
  html, body {
    width: 1200px;
    height: 780px;
    overflow: hidden;
    background: var(--page-bg);
    font-family: var(--font-text);
  }
  .canvas {
    position: relative;
    width: 1200px;
    height: 780px;
  }
  .card {
    position: absolute;
    top: 235px;
    width: 530px;
    height: 310px;
    border-radius: var(--card-radius);
    overflow: hidden;
    box-shadow: 0 8px 22px rgba(20, 40, 60, 0.18);
  }
  .card-front { left: 50px; background: var(--card-white); }
  .card-back {
    left: 620px;
    background: linear-gradient(135deg, var(--blue-light) 0%, var(--blue-mid) 45%, var(--blue-deep) 100%);
  }
  .card-art {
    position: absolute;
    inset: 0;
    width: 100%;
    height: 100%;
  }

  /* Front */
  .front-wordmark {
    position: absolute;
    left: 40px;
    top: 58px;
    font-size: 36px;
    font-weight: 700;
    color: var(--logo-grey);
    letter-spacing: 0.5px;
  }
  .contact-block {
    position: absolute;
    left: 30px;
    bottom: 26px;
    color: var(--ink-white);
  }
  .contact-name {
    font-size: 19px;
    font-weight: 400;
    text-transform: uppercase;
    letter-spacing: 0.3px;
    line-height: 1.05;
  }
  .contact-title {
    font-size: 15px;
    line-height: 1.1;
    margin-bottom: 10px;
  }
  .contact-line {
    display: flex;
    align-items: center;
    gap: 7px;
    font-size: 15px;
    line-height: 1.35;
  }
  .contact-icon { width: 13px; height: 13px; flex: none; }
  .front-website {
    position: absolute;
    right: 26px;
    top: 124px;
    font-size: 15px;
    color: var(--ink-white);
  }

  /* Back */
  .back-wordmark {
    position: absolute;
    left: 0;
    right: 0;
    top: 108px;
    text-align: center;
    font-size: 42px;
    font-weight: 700;
    color: var(--ink-white);
    letter-spacing: 0.5px;
  }
  .services {
    position: absolute;
    left: 60px;
    top: 196px;
    color: var(--ink-white);
  }
  .services-heading {
    font-size: 14px;
    text-transform: uppercase;
    letter-spacing: 0.5px;
    margin-bottom: 4px;
  }
  .services-list { font-size: 15px; }
</style>
</head>
<body>
<main class="canvas">

  <section class="card card-front" aria-label="Business card front">
    <svg class="card-art" viewBox="0 0 530 310" preserveAspectRatio="none" aria-hidden="true">
      <defs>
        <linearGradient id="frontBlue" x1="0" y1="1" x2="1" y2="0">
          <stop offset="0" stop-color="#1a8fc0"/>
          <stop offset="0.55" stop-color="#22b6d6"/>
          <stop offset="1" stop-color="#1a8fc0"/>
        </linearGradient>
        <linearGradient id="frontGrey" x1="0" y1="0" x2="1" y2="0">
          <stop offset="0" stop-color="#e6e8ea"/>
          <stop offset="1" stop-color="#a9adb2"/>
        </linearGradient>
      </defs>
      <path class="swoosh-grey" fill="url(#frontGrey)"
            d="M0,180 C150,186 245,166 322,96 C382,40 445,6 530,-4 L530,310 L0,310 Z"/>
      <path class="swoosh-white" fill="#f7f8f9"
            d="M0,188 C150,194 250,174 328,104 C388,50 450,16 530,6 L530,310 L0,310 Z"/>
      <path class="swoosh-blue" fill="url(#frontBlue)"
            d="M0,194 C152,200 254,180 333,110 C393,56 452,22 530,12 L530,310 L0,310 Z"/>
    </svg>

    <div class="front-wordmark">Brambury Logistics</div>

    <div class="front-website">www.bramburylogistics.com.au</div>

    <div class="contact-block">
      <p class="contact-name">Jon Harlow</p>
      <p class="contact-title">Managing director</p>
      <p class="contact-line">
        <svg class="contact-icon" viewBox="0 0 14 14" aria-hidden="true">
          <rect width="14" height="14" rx="2.5" fill="#ffffff"/>
          <path d="M4.2,3 L5.6,3 L6.3,5 L5.3,5.8 C5.8,6.9 6.8,8 8,8.6 L8.8,7.6 L10.8,8.3 L10.8,9.8 C10.8,10.4 10.3,10.9 9.7,10.8 C6.3,10.4 3.6,7.7 3.2,4.3 C3.1,3.6 3.6,3 4.2,3 Z" fill="#1a8fc0"/>
        </svg>
        <span>0412558036</span>
      </p>
      <p class="contact-line">
        <svg class="contact-icon" viewBox="0 0 14 14" aria-hidden="true">
          <rect width="14" height="14" rx="2.5" fill="#ffffff"/>
          <rect x="2.5" y="4" width="9" height="6.5" fill="none" stroke="#1a8fc0" stroke-width="1.2"/>
          <path d="M2.5,4 L7,7.8 L11.5,4" fill="none" stroke="#1a8fc0" stroke-width="1.2"/>
        </svg>
        <span>dane@bramburylogistics.com.au</span>
      </p>
    </div>
  </section>

  <section class="card card-back" aria-label="Business card back">
    <div class="back-wordmark">Brambury Logistics</div>
    <div class="services">
      <p class="services-heading">Services</p>
      <p class="services-list">Tamo Trucks | Transport | Contract Logistics</p>
    </div>
  </section>

</main>
</body>
</html>
```